BoardLinkHub.golf Newsletter

A newsletter template for BoardLinkHub.golf, a new member networking group . (www.boardlinkhub.golf. The template must be easily formatted with the ability for me to drop in images and news. Typically 4-5 content sections a week. These will include video and podcasts. The content needs to be divided into sections-
Governance
Food and Beverage,
Course Management
News
Golf Club Operations
Membership and Marketing
Events
Not every section will have content every week so they need to be interchangeable. The stories will have the first couple of lines and then a Read here to take them to the member area of the website.
There needs to be an introduction section each week of 3-4 lines so we can pick out the highlights.
The bottom section needs to have contact details and links to LinkedIN and our own app on the apple/google stores.
The style needs to be professional and modern.

Target Market(s)

B2B golf club directors

Requirements
Should not have
• Not a lot of golf imagery. It is not for golfers

```html
<!DOCTYPE html>
<html lang="en">
<head>
<meta charset="utf-8">
<title>BoardLinkHub.golf Newsletter</title>
<link href="https://fonts.googleapis.com/css2?family=Roboto:wght@300;400;500;700&family=Roboto+Condensed:wght@300;400&display=swap" rel="stylesheet">
<style>
:root{
  --page:#e9e9e9;
  --paper:#ffffff;
  --navy:#043d78;
  --ink:#0b3c73;
  --body:#3b3b3b;
  --footer:#d4d4d4;
  --olive:#d9dca6;
}
*{margin:0;padding:0;box-sizing:border-box}
html,body{width:1200px;height:2807px;overflow:hidden;background:var(--page);font-family:"Roboto",sans-serif}
.newsletter{position:absolute;left:126px;top:0;width:948px;height:2759px;background:var(--paper)}
.hero{position:absolute;left:0;top:0;width:948px;height:723px}
.hero svg{display:block}
.brand{position:absolute;left:8px;top:7px;width:272px;height:91px;background:#fff;display:flex;align-items:center;justify-content:center}
.brand-name{font-weight:500;font-size:28px;color:var(--ink)}
.hero-title{position:absolute;left:25px;top:316px;width:520px;font-family:"Roboto Condensed",sans-serif;font-weight:400;font-size:33px;line-height:44px;color:#fff;text-shadow:0 2px 4px rgba(0,0,0,.45)}
.intro{position:absolute;left:0;top:733px;width:948px;text-align:center;font-weight:500;font-size:23.5px;line-height:33.5px;color:var(--ink)}
.sections{position:absolute;left:20px;top:856px;width:910px}
.topic{height:176px;position:relative}
.topic-head{display:flex;align-items:center;gap:10px;height:56px}
.topic-head svg{flex:none}
.topic-title{font-size:33px;font-weight:400;color:var(--ink)}
.topic-text{font-size:19.5px;line-height:28px;color:var(--body);margin-top:6px}
.read-more{position:absolute;right:26px;top:142px;width:160px;height:42px;border-radius:21px;background:var(--navy);color:#fff;font-size:19px;text-decoration:none;display:flex;align-items:center;justify-content:center;gap:10px}
.mission{position:absolute;left:19px;top:2174px;width:908px;height:207px;background:var(--navy);color:#fff;font-weight:300;font-size:33px;line-height:46px;text-align:center;display:flex;align-items:center;justify-content:center;padding:0 20px}
.stores{position:absolute;top:2458px;left:244px;display:flex;gap:12px}
.store{width:224px;height:71px;border-radius:9px;background:#000;border:2px solid #a6a6a6}
.site-footer{position:absolute;left:0;top:2605px;width:948px;height:112px;background:var(--footer);display:flex;align-items:center;justify-content:space-between;padding:0 21px 0 17px}
.copyright{font-size:16.5px;color:#333}
.social{display:flex;gap:4px}
.social a{width:37px;height:37px;border-radius:50%;border:2px solid #222;display:block}
</style>
</head>
<body>
<main class="newsletter">
  <header class="hero">
    <svg width="948" height="723" viewBox="0 0 948 723">
      <defs>
        <linearGradient id="lawn" x1="0" y1="0" x2="0" y2="1">
          <stop offset="0" stop-color="#3f5a2a"/>
          <stop offset=".35" stop-color="#7a9a3c"/>
          <stop offset="1" stop-color="#a9bd4e"/>
        </linearGradient>
      </defs>
      <rect width="948" height="723" fill="url(#lawn)" role="img" aria-label="Photo of a person sitting on a golf course lawn"/>
      <path d="M0 470 C90 600 230 650 330 680 C430 700 480 600 560 590 C680 580 800 690 948 723 L948 723 L0 723 Z" fill="var(--olive)"/>
      <path d="M0 490 C100 620 240 670 340 690 C440 708 490 620 570 615 C690 610 810 700 948 723 L0 723 Z" fill="#fff"/>
    </svg>
    <div class="brand"><span class="brand-name">BoardLinkHub</span></div>
    <h1 class="hero-title">Welcome to the BoardLinkHub<br>the largest community of private<br>golf club directors in the<br>UK and Ireland.</h1>
  </header>

  <p class="intro">BoardLinkHub was founded in 2018 and now has more than<br>500 members.&nbsp; We are Independent- run on behalf of<br>private golf clubs and their directors.</p>

  <section class="sections">
    <article class="topic">
      <div class="topic-head"><svg width="48" height="54" viewBox="0 0 48 54" fill="none" stroke="#0b3c73" stroke-width="2.5"><path d="M4 20 L24 8 L44 20 Z M6 22h36 M10 24v20 M18 24v20 M30 24v20 M38 24v20 M4 46h40 M2 51h44 M24 8V1h8v5h-8"/></svg><h2 class="topic-title">Governance</h2></div>
      <p class="topic-text">Helping clubs develop successful and effective boards that are well prepared for the future through educational programme and materials focused on best practice and successful industry trends</p>
      <a class="read-more" href="#">Read More <span>⟶</span></a>
    </article>
    <article class="topic">
      <div class="topic-head"><svg width="64" height="54" viewBox="0 0 64 54" fill="none" stroke="#0b3c73" stroke-width="2.5"><path d="M4 36 C4 24 36 24 36 36 Z M3 40h34 M4 44h32 v4 h-32 Z M40 20h20 l-3 32h-14 Z M52 20 l4-16 h6"/></svg><h2 class="topic-title">Food and Beverage</h2></div>
      <p class="topic-text">Helping clubs develop successful and effective boards that are well prepared for the future through educational programme and materials focused on best practice and successful industry trends</p>
      <a class="read-more" href="#">Read More <span>⟶</span></a>
    </article>
    <article class="topic">
      <div class="topic-head"><svg width="52" height="48" viewBox="0 0 52 48" fill="none" stroke="#0b3c73" stroke-width="2.5"><rect x="2" y="2" width="48" height="42"/><path d="M2 9h48 M8 16h12 M8 23h12 M8 30h12"/><circle cx="33" cy="25" r="7"/><path d="M24 42 C24 34 42 34 42 42"/></svg><h2 class="topic-title">Course Management</h2></div>
      <p class="topic-text">Helping clubs develop successful and effective boards that are well prepared for the future through educational programme and materials focused on best practice and successful industry trends</p>
      <a class="read-more" href="#">Read More <span>⟶</span></a>
    </article>
    <article class="topic">
      <div class="topic-head"><svg width="62" height="48" viewBox="0 0 62 48" fill="none" stroke="#0b3c73" stroke-width="2.5"><path d="M10 4h50v38a4 4 0 0 1-4 4H6a4 4 0 0 1-4-4V14h8 M10 4v38"/><rect x="16" y="20" width="14" height="14"/><path d="M36 20h18 M36 27h18 M36 34h18 M16 40h38 M16 11h38"/></svg><h2 class="topic-title">News</h2></div>
      <p class="topic-text">Helping clubs develop successful and effective boards that are well prepared for the future through educational programme and materials focused on best practice and successful industry trends</p>
      <a class="read-more" href="#">Read More <span>⟶</span></a>
    </article>
    <article class="topic">
      <div class="topic-head"><svg width="52" height="52" viewBox="0 0 52 52" fill="none" stroke="#0b3c73" stroke-width="2.5"><path d="M24 36V2 l14 7 -14 7"/><ellipse cx="26" cy="40" rx="23" ry="9"/><ellipse cx="24" cy="39" rx="4" ry="2"/><circle cx="12" cy="42" r="2"/></svg><h2 class="topic-title">Golf Club Operations</h2></div>
      <p class="topic-text">Helping clubs develop successful and effective boards that are well prepared for the future through educational programme and materials focused on best practice and successful industry trends</p>
      <a class="read-more" href="#">Read More <span>⟶</span></a>
    </article>
    <article class="topic">
      <div class="topic-head"><svg width="56" height="50" viewBox="0 0 56 50" fill="none" stroke="#0b3c73" stroke-width="2.5"><rect x="2" y="10" width="52" height="38" rx="3"/><rect x="22" y="2" width="12" height="12" rx="2"/><circle cx="18" cy="26" r="5"/><path d="M9 40 C9 32 27 32 27 40 Z M34 24h14 M34 31h14 M34 38h14"/></svg><h2 class="topic-title">Membership and Marketing</h2></div>
      <p class="topic-text">Helping clubs develop successful and effective boards that are well prepared for the future through educational programme and materials focused on best practice and successful industry trends</p>
      <a class="read-more" href="#">Read More <span>⟶</span></a>
    </article>
    <article class="topic">
      <div class="topic-head"><svg width="56" height="54" viewBox="0 0 56 54" fill="none" stroke="#0b3c73" stroke-width="3"><rect x="3" y="7" width="50" height="44"/><path d="M14 2v10 M28 2v10 M42 2v10 M11 22h20 M11 31h26 M11 40h34 M37 20l4 4 7-8"/></svg><h2 class="topic-title">Events</h2></div>
      <p class="topic-text">Helping clubs develop successful and effective boards that are well prepared for the future through educational programme and materials focused on best practice and successful industry trends</p>
      <a class="read-more" href="#">Read More <span>⟶</span></a>
    </article>
  </section>

  <aside class="mission">Provide a collaborative platform for private member<br>club directors and those who want to partner with them<br>to share their expertise and learnings</aside>

  <div class="stores">
    <a class="store" href="#" aria-label="Get the mobile app"></a>
    <a class="store" href="#" aria-label="Download the mobile app"></a>
  </div>

  <footer class="site-footer">
    <p class="copyright">Copyright © 2021&nbsp; BoardLinkHub.golf - All Right Reserved.</p>
    <nav class="social">
      <a href="#" aria-label="Social profile"></a>
      <a href="#" aria-label="Social profile"></a>
      <a href="#" aria-label="Professional network profile"></a>
    </nav>
  </footer>
</main>
</body>
</html>
```